Healthcare Comms Consultant Needs Scroll Down Website

Would like a modern scroll down website/ site on one page. Would like a gallery at the top. Followed by my bio and capabilities section. Pretty simple. Just want it look pretty/ clean. Example of similar site - https://7qrstudio.com. I live in San Diego so would be neat to bring in some water elements. And I surf.

Target Market(s)

US biotech, Medtech companies

Industry/Entity Type

Healthcare

Coding

Coded - Design and coding required

Number of Pages Required

1 page

Font styles to use
Sans Serif

Requirements
Must have
• A logo, gallery section (I have the photos) with one large pic of me in the center (Brintex), short list of capabilities (I have text), my bio (I have this text). How to contact me at the bottom and a link to my Proflume profile.

```html
<!DOCTYPE html>
<html lang="en">
<head>
<meta charset="utf-8">
<title>Tidewell Media — Healthcare PR | Media Consultant</title>
<link href="https://fonts.googleapis.com/css2?family=Lato:wght@400;700&display=swap" rel="stylesheet">
<style>
  :root {
    --blue: #1b9fe0;
    --blue-deep: #1a7fb4;
    --navy: #2b2690;
    --ink: #3a3a3a;
    --form-bar: #2f86a9;
    --form-field: #e4e8ec;
    --white: #ffffff;
  }
  * { box-sizing: border-box; margin: 0; padding: 0; }
  html, body { width: 1200px; height: 3676px; overflow: hidden; background: var(--white); }
  body { position: relative; font-family: "Lato", sans-serif; color: var(--navy); }

  .site-header { position: absolute; top: 0; left: 0; width: 1200px; height: 90px; }
  .brand-small { position: absolute; left: 100px; top: 28px; display: flex; align-items: center; gap: 10px; }
  .brand-small .brand-square { width: 30px; height: 30px; background: var(--blue); }
  .brand-small .brand-name { font-size: 24px; font-weight: 700; color: var(--blue); }
  .main-nav { position: absolute; left: 730px; top: 37px; display: flex; gap: 9px; }
  .main-nav a { font-size: 15px; font-weight: 700; color: var(--navy); text-decoration: none; letter-spacing: .3px; }
  .social-header { position: absolute; left: 1047px; top: 16px; display: flex; align-items: center; gap: 6px; text-decoration: none; }
  .social-dot { display: block; border-radius: 50%; background: var(--blue-deep); }
  .social-header .social-dot { width: 56px; height: 56px; }
  .social-name { font-size: 13px; font-weight: 700; color: var(--navy); }

  .hero { position: absolute; top: 90px; left: 0; width: 1200px; height: 821px; }
  .hero-portrait { position: absolute; left: 630px; top: 60px; width: 355px; height: 761px;
    border-radius: 150px 150px 0 0; background: linear-gradient(180deg, #e8d3b4 0%, #f3f1ee 35%, #ece9e4 70%, #9a9a9a 100%); }
  .hero-brand { position: absolute; left: 185px; top: 475px; display: flex; align-items: center; gap: 18px; }
  .hero-brand .brand-square { width: 90px; height: 90px; background: var(--blue); }
  .hero-brand .brand-name { font-size: 38px; font-weight: 700; color: var(--blue); line-height: 1.05; }
  .hero-tagline { position: absolute; left: 123px; top: 638px; font-size: 24px; color: var(--ink); letter-spacing: .2px; }
  .btn { display: inline-block; background: var(--blue); color: var(--white); border-radius: 6px; text-align: center; font-weight: 400; text-decoration: none; }
  .hero-cta { position: absolute; left: 205px; top: 707px; width: 200px; height: 50px; line-height: 50px; font-size: 24px; }

  .gallery { position: absolute; top: 911px; left: 0; width: 1200px; height: 789px; display: grid;
    grid-template-columns: 427px 370px 403px; grid-template-rows: 246px 263px 280px; }
  .gallery-item { display: block; }
  .g1 { background: linear-gradient(135deg, #c9a877, #3b5c8f); }
  .g2 { background: linear-gradient(135deg, #4a4a4a, #b9a58d); }
  .g3 { background: linear-gradient(135deg, #e9e3ee, #7a6a8a); }
  .g4 { background: linear-gradient(135deg, #e6cf9a, #5a6f93); }
  .g5 { background: linear-gradient(135deg, #3a4a6a, #c89a5a); }
  .g6 { background: linear-gradient(135deg, #5e4a30, #3c5a9a); }
  .g7 { background: linear-gradient(135deg, #28508f, #e7dcc8); }
  .g8 { background: linear-gradient(135deg, #d9c39e, #5a6e86); }
  .g9 { background: linear-gradient(135deg, #8d5aa8, #3c3a4a); }

  .bio { position: absolute; top: 1780px; left: 0; width: 1200px; }
  .section-title { text-align: center; color: var(--blue); font-weight: 400; }
  .bio .section-title { font-size: 56px; margin-left: 30px; }
  .bio-text { position: absolute; left: 87px; top: 78px; width: 1020px; font-size: 19px; line-height: 25px; color: var(--navy); }
  .bio-text p + p { margin-top: 25px; }

  .capabilities { position: absolute; top: 2226px; left: 0; width: 1200px; height: 761px;
    border-top: 3px solid var(--blue); border-bottom: 3px solid var(--blue);
    background: radial-gradient(ellipse at 55% 35%, #5fa3c8 0%, #2e88b6 45%, #1f6f9c 100%); color: var(--white); text-align: center; }
  .capabilities h2 { position: absolute; top: 380px; width: 100%; font-size: 56px; font-weight: 400; left: -10px; }
  .capabilities .lead { position: absolute; top: 472px; width: 100%; font-size: 25px; }
  .capabilities ul { position: absolute; top: 530px; width: 100%; list-style: none; font-size: 20px; line-height: 25px; left: -10px; }

  .contact { position: absolute; top: 3040px; left: 0; width: 1200px; height: 560px; }
  .contact .section-title { font-size: 60px; font-weight: 700; margin-left: -30px; }
  .contact-form { position: absolute; left: 40px; top: 128px; width: 487px; }
  .field-label { height: 36px; background: var(--form-bar); color: var(--white); font-size: 12px; font-style: italic;
    display: flex; align-items: center; gap: 12px; padding-left: 30px; }
  .field-label .ico { width: 14px; height: 14px; border-radius: 50%; background: rgba(255,255,255,.8); }
  .field-input { height: 28px; background: var(--form-field); }
  .field-message { height: 105px; background: var(--form-bar); color: var(--white); font-size: 11px; font-style: italic; padding: 14px 0 0 35px; }
  .form-send { position: absolute; left: 155px; top: 463px; width: 200px; height: 50px; line-height: 50px; font-size: 24px; }

  .contact-details { position: absolute; left: 700px; top: 0; width: 470px; height: 560px; text-align: center; }
  .contact-details .icon { position: absolute; left: 50%; transform: translateX(-50%); }
  .contact-details .mail-icon { top: 128px; }
  .contact-details .phone-icon { top: 249px; }
  .contact-details .detail { position: absolute; left: 0; width: 100%; font-size: 28px; font-weight: 700; color: var(--navy); text-decoration: none; }
  .contact-details .email { top: 196px; }
  .contact-details .phone { top: 335px; }
  .social-contact { position: absolute; left: 0; top: 399px; width: 100%; display: flex; align-items: center; justify-content: center; gap: 10px; text-decoration: none; }
  .social-contact .social-dot { width: 88px; height: 88px; }

  .site-footer { position: absolute; top: 3600px; left: 0; width: 1200px; height: 76px; background: var(--blue);
    color: var(--white); text-align: center; font-size: 24px; font-weight: 700; line-height: 76px; }
</style>
</head>
<body>

<header class="site-header">
  <div class="brand-small"><span class="brand-square"></span><span class="brand-name">Tidewell</span></div>
  <nav class="main-nav">
    <a href="#bio">BIO</a><a href="#gallery">GALLERY</a><a href="#capabilities">CAPABILITIES</a><a href="#contact">CONTACT</a>
  </nav>
  <a class="social-header" href="#" aria-label="Proflume profile"><span class="social-dot"></span><span class="social-name">Proflume</span></a>
</header>

<section class="hero">
  <div class="hero-portrait" role="img" aria-label="Portrait of Marisa in a white blazer and coral top"></div>
  <div class="hero-brand"><span class="brand-square"></span><span class="brand-name">Tidewell<br>Media</span></div>
  <p class="hero-tagline">HEALTHCARE PR | MEDIA CONSULTANT</p>
  <a class="btn hero-cta" href="#bio">LEARN MORE</a>
</section>

<section class="gallery" id="gallery">
  <div class="gallery-item g1" role="img" aria-label="Marisa at a conference interview set"></div>
  <div class="gallery-item g2" role="img" aria-label="Marisa speaking with a microphone holding an award"></div>
  <div class="gallery-item g3" role="img" aria-label="Marisa holding an award at a media wall"></div>
  <div class="gallery-item g4" role="img" aria-label="Marisa with a camera operator"></div>
  <div class="gallery-item g5" role="img" aria-label="Marisa at a large health conference hall"></div>
  <div class="gallery-item g6" role="img" aria-label="Broadcast interview set with lighting"></div>
  <div class="gallery-item g7" role="img" aria-label="Marisa with a colleague at an industry event"></div>
  <div class="gallery-item g8" role="img" aria-label="Headshot of Marisa"></div>
  <div class="gallery-item g9" role="img" aria-label="Marisa at an oncology congress in Barcelona"></div>
</section>

<section class="bio" id="bio">
  <h2 class="section-title">BIO</h2>
  <div class="bio-text">
    <p>Marisa is a global health industry connector and creative problem solver. She has worked on some of the world's biggest therapies and medical technologies, including the first RNAi therapy (Corvane's NERAVIX), the first therapy for Duchenne Muscular Dystrophy (Helvion's MYOLINK 42), the first technology in the world to personalize insulin 24 hrs. a day (Pulsera's GlucoSync 540) and Quantora's AI launch into healthcare (Sage). She has counseled some of the most well-known health/ technology organizations and developed communications strategies for the world's biggest brands (Barrow &amp; Lane, BLABS, B&amp;L Innovation, Pulsera, Meridex, Quantora, Voltmart, Kanoro, Aurelis, Dunmere, Harborview &amp; Hale, NPHS), but she is most proud of her work telling patient stories.</p>
    <p>Marisa excels at working with the media to bring health stories to life while making them accessible to stakeholders. She worked as a journalist before transitioning to communications and has special insight in working with the media. With 15-years of communications experience, she is consistently leveraging her long-standing relationships</p>
  </div>
</section>

<section class="capabilities" id="capabilities" role="img" aria-label="Marisa speaking on stage with a microphone, blue tinted">
  <h2>Tidewell Media Capabilities</h2>
  <p class="lead">Providing senior level support for elite pharma/ biotech/ healthcare companies at all stages of development.</p>
  <ul>
    <li>Expert Media Relations</li>
    <li>Corporate Thought Leadership</li>
    <li>Executive Visibility</li>
    <li>Narrative Development</li>
    <li>Crisis Management</li>
    <li>Drug/ and Device Product Development</li>
    <li>Narrative Development</li>
  </ul>
</section>

<section class="contact" id="contact">
  <h2 class="section-title">CONTACT</h2>
  <form class="contact-form">
    <div class="field-label"><span class="ico"></span>Name...</div>
    <div class="field-input"></div>
    <div class="field-label"><span class="ico"></span>Email...</div>
    <div class="field-input"></div>
    <div class="field-label"><span class="ico"></span>Website...</div>
    <div class="field-input"></div>
    <div class="field-message">Type your message here...</div>
  </form>
  <a class="btn form-send" href="#">SEND</a>

  <div class="contact-details">
    <svg class="icon mail-icon" width="80" height="48" viewBox="0 0 80 48" aria-hidden="true">
      <rect x="2" y="2" width="76" height="44" fill="none" stroke="#1b9fe0" stroke-width="3"/>
      <path d="M2 2 L40 30 L78 2" fill="none" stroke="#1b9fe0" stroke-width="3"/>
      <path d="M2 46 L30 22 M78 46 L50 22" fill="none" stroke="#1b9fe0" stroke-width="3"/>
    </svg>
    <a class="detail email" href="mailto:Marisa@TidewellMedia.com">Marisa@TidewellMedia.com</a>
    <svg class="icon phone-icon" width="86" height="58" viewBox="0 0 86 58" aria-hidden="true">
      <path d="M4 20 Q4 4 43 4 Q82 4 82 20 L82 26 L62 26 L62 16 L24 16 L24 26 L4 26 Z" fill="#1b9fe0"/>
      <path d="M24 24 L62 24 L76 56 L10 56 Z" fill="#1b9fe0"/>
      <circle cx="43" cy="40" r="8" fill="#ffffff"/>
    </svg>
    <a class="detail phone" href="tel:+15550142290">+1-555-014-2290</a>
    <a class="social-contact" href="#" aria-label="Proflume profile"><span class="social-dot"></span><span class="social-name">Proflume</span></a>
  </div>
</section>

<footer class="site-footer">copyright 2020 @&nbsp; TidewellMedia.com</footer>

</body>
</html>
```